Business Card Design

I need a business card for company that is a limited company that was originally an off-road vehicle company (atv's side by sides snowmobiles and motorcycles) and I have recently sold the assets of the company that was operating under a different name and have become semi retired. I continue to do maintenance on these types of vehicles and also sell and install parts and accessories. Recently I have also contracted to a snowmobile club to operate their groomer to groom the snowmobile trails. I would like bright and bold colors.
Industry/Entity Type
Club
Contact Information for Business Card
KTV Holdings Ltd.
Milo Fenwick
780-413-2769

```html
<!DOCTYPE html>
<html lang="en">
<head>
<meta charset="utf-8">
<title>KTV Holdings Ltd. — Business Card</title>
<link rel="stylesheet" href="https://fonts.googleapis.com/css2?family=Libre+Baskerville:wght@400;700&display=swap">
<style>
  :root {
    --page: #ecebef;
    --card-white: #f7f7f8;
    --card-white-edge: #e4e4e8;
    --purple-deep: #2c2a66;
    --purple-mid: #3f3d86;
    --purple-light: #5b58a6;
    --ink-light: #ffffff;
    --ghost: #dcdcdf;
    --brand: #3a3880;
  }
  * { box-sizing: border-box; margin: 0; padding: 0; }
  html, body { width: 1200px; height: 1023px; overflow: hidden; }
  body {
    background: var(--page);
    font-family: "Libre Baskerville", "Times New Roman", serif;
    position: relative;
  }
  .card {
    position: absolute;
    left: 250px;
    width: 700px;
    height: 400px;
    border-radius: 4px;
    overflow: hidden;
    box-shadow: 0 10px 28px rgba(30, 28, 70, 0.22);
  }

  /* Front */
  .card-front { top: 70px; background: var(--card-white); }
  .front-upper {
    position: absolute; inset: 0 0 150px 0;
    background: linear-gradient(180deg, var(--card-white) 0%, var(--card-white-edge) 100%);
  }
  .rider-art {
    position: absolute;
    background: linear-gradient(160deg, var(--ghost), #e9e9ec);
    border-radius: 40% 50% 30% 45%;
    opacity: 0.8;
  }
  .rider-art.left { left: 40px; bottom: 12px; width: 150px; height: 120px; }
  .rider-art.right { right: 40px; top: 20px; width: 130px; height: 140px; }

  .brand {
    position: absolute; left: 50%; top: 125px;
    transform: translate(-50%, -50%);
    display: flex; align-items: center; gap: 18px;
  }
  .brand-dot {
    width: 70px; height: 70px; border-radius: 50%;
    background: var(--brand);
  }
  .brand-name {
    font-weight: 700; font-size: 34px; color: var(--brand);
    white-space: nowrap;
  }

  .front-band {
    position: absolute; left: 0; right: 0; bottom: 0; height: 150px;
    background: linear-gradient(180deg, var(--purple-light) 0%, var(--purple-mid) 55%, var(--purple-deep) 100%);
    display: flex; align-items: center; justify-content: space-between;
    padding: 0 44px;
    color: var(--ink-light);
  }
  .person-name { font-size: 28px; }
  .phone { display: flex; align-items: center; gap: 12px; font-size: 30px; }
  .phone svg { width: 22px; height: 30px; }

  /* Back */
  .card-back {
    top: 540px;
    background: linear-gradient(90deg, var(--purple-deep) 0%, var(--purple-mid) 30%, var(--purple-light) 50%, var(--purple-mid) 70%, var(--purple-deep) 100%);
  }
  .card-back .brand { top: 200px; }
  .card-back .brand-dot { background: var(--ink-light); }
  .card-back .brand-name { color: var(--ink-light); }
</style>
</head>
<body>
  <section class="card card-front" aria-label="Business card front">
    <div class="front-upper">
      <div class="rider-art left" role="img" aria-label="Faint silhouette of a motocross rider"></div>
      <div class="rider-art right" role="img" aria-label="Faint silhouette of a snowmobile rider"></div>
      <div class="brand">
        <span class="brand-dot"></span>
        <span class="brand-name">KTV Holdings Ltd.</span>
      </div>
    </div>
    <div class="front-band">
      <span class="person-name">Milo Fenwick</span>
      <span class="phone">
        <svg viewBox="0 0 22 30" aria-hidden="true">
          <rect x="1.5" y="1.5" width="19" height="27" rx="3" fill="none" stroke="#fff" stroke-width="3"/>
          <rect x="5" y="6" width="12" height="15" fill="#fff"/>
        </svg>
        780-413-2769
      </span>
    </div>
  </section>

  <section class="card card-back" aria-label="Business card back">
    <div class="brand">
      <span class="brand-dot"></span>
      <span class="brand-name">KTV Holdings Ltd.</span>
    </div>
  </section>
</body>
</html>
```